Business Card - connecting 2 souls and beggining the journey of self discovery

Logo on the front
with tag line

On the back list of services and contact details

Seminars
workshops
Coaching
podcasts

Daniel Porthwick
Health & Wellbeing Life Coach
0491 372 815
daniel@wovenpathwellness.example
wovenpathwellness.example

Industry/Entity Type

Life Coaching

Contact Information for Business Card

I like the use of colour from the logo to be used. I'm not a fan of white.

Requirements
Must have
• My tagline: The journey home starts with you
Nice to have
• Use of colour that is in the Woven Path logo

```html
<!DOCTYPE html>
<html lang="en">
<head>
<meta charset="UTF-8">
<title>Woven Path Wellness – Business Card</title>
<link rel="stylesheet" href="https://fonts.googleapis.com/css2?family=Questrial&display=swap">
<style>
  :root {
    --page-bg: #ffffff;
    --card-bg: #333333;
    --band-purple: #9a5ba6;
    --text-light: #ffffff;
    --text-soft: #f1eaf3;
    --figure-tone: rgba(200, 200, 200, 0.16);
    --mark-purple: #8d4fb8;
  }
  * { box-sizing: border-box; margin: 0; padding: 0; }
  html, body {
    width: 1200px;
    height: 362px;
    overflow: hidden;
    background: var(--page-bg);
    font-family: "Questrial", "Century Gothic", sans-serif;
  }
  .canvas {
    position: relative;
    width: 1200px;
    height: 362px;
  }
  .card {
    position: absolute;
    top: 36px;
    width: 509px;
    height: 283px;
    background: var(--card-bg);
    overflow: hidden;
  }
  .card--front { left: 39px; }
  .card--back { left: 652px; }

  .meditation-figure {
    position: absolute;
    background: linear-gradient(180deg, rgba(200,200,200,0) 0%, var(--figure-tone) 45%, rgba(200,200,200,0.08) 100%);
    border-radius: 40px 40px 6px 6px;
  }
  .meditation-figure--left { left: 0; top: 68px; width: 106px; height: 166px; }
  .meditation-figure--right { right: 0; top: 68px; width: 106px; height: 166px; }

  .band {
    position: absolute;
    left: 0;
    top: 232px;
    width: 100%;
    height: 20px;
    background: var(--band-purple);
    color: var(--text-soft);
    font-style: italic;
    font-size: 13.5px;
    line-height: 20px;
    text-align: center;
    letter-spacing: 0.2px;
  }

  .brand {
    position: absolute;
    left: 0;
    top: 30px;
    width: 100%;
    text-align: center;
  }
  .brand__dot {
    display: block;
    margin: 0 auto;
    width: 78px;
    height: 78px;
    border-radius: 50%;
    background: var(--mark-purple);
  }
  .brand__name {
    display: block;
    margin-top: 14px;
    color: var(--text-light);
    font-size: 22px;
    letter-spacing: 3px;
  }
  .brand__descriptor {
    position: absolute;
    left: 0;
    top: 178px;
    width: 100%;
    text-align: center;
    color: var(--text-light);
    font-size: 15px;
    letter-spacing: 0.3px;
  }

  .contact {
    position: absolute;
    left: 43px;
    top: 76px;
    color: var(--text-light);
    font-size: 15.5px;
    line-height: 19px;
    font-style: normal;
  }
  .contact__name { font-weight: 700; font-size: 16px; letter-spacing: 0.2px; }
</style>
</head>
<body>
<main class="canvas">
  <section class="card card--front" aria-label="Card front">
    <div class="meditation-figure meditation-figure--left" role="img" aria-label="Faint outline of a person seated in meditation"></div>
    <div class="meditation-figure meditation-figure--right" role="img" aria-label="Faint outline of a person seated in meditation"></div>
    <div class="brand">
      <span class="brand__dot" aria-hidden="true"></span>
      <span class="brand__name">WOVEN PATH</span>
    </div>
    <p class="brand__descriptor">HOME OF HOLISTIC HEALTH</p>
    <p class="band">“The journey home starts with you”...</p>
  </section>

  <section class="card card--back" aria-label="Card back">
    <div class="meditation-figure meditation-figure--right" role="img" aria-label="Faint outline of a person seated in meditation"></div>
    <address class="contact">
      <div class="contact__name">Daniel Porthwick</div>
      <div>Health &amp; Wellbeing Life Coach</div>
      <div>0491 372 815</div>
      <div>daniel@wovenpathwellness.example</div>
      <div>wovenpathwellness.example</div>
    </address>
    <p class="band">Seminars, Workshops, Coaching, Podcast</p>
  </section>
</main>
</body>
</html>
```